Solar appointment reminder card

We are looking for a new design for our appointment reminder card since we have changed our logo. The card should have the new logo along with space for the employee to hand write the customers appointment date, time, the employees name and phone number.
I've uploaded what our old basic appointment card looked like and our new logo.

The cards should be in a standard business card size and could be horizontal or vertical.

```html
<!DOCTYPE html>
<html lang="en">
<head>
<meta charset="UTF-8">
<title>Sunridge Solar – Appointment Card</title>
<link href="https://fonts.googleapis.com/css2?family=Montserrat:wght@500;800&display=swap" rel="stylesheet">
<style>
  :root {
    --page-white: #ffffff;
    --card-yellow: #f5bc1c;
    --card-yellow-light: #f8c423;
    --card-yellow-dark: #eeb316;
    --frame-white: #ffffff;
    --ink: #141414;
  }
  * { margin: 0; padding: 0; box-sizing: border-box; }
  html, body {
    width: 1200px;
    height: 686px;
    overflow: hidden;
    background: var(--page-white);
  }
  .page {
    position: relative;
    width: 1200px;
    height: 686px;
    font-family: "Montserrat", Arial, sans-serif;
    color: var(--ink);
  }
  .card {
    position: absolute;
    left: 41px;
    top: 41px;
    width: 1118px;
    height: 603px;
    background: radial-gradient(ellipse at 50% 45%, var(--card-yellow-light) 0%, var(--card-yellow) 70%, var(--card-yellow-dark) 100%);
  }
  .card__frame {
    position: absolute;
    left: 66px;
    top: 65px;
    width: 1063px;
    height: 550px;
    border: 15px solid var(--frame-white);
  }
  .brand-name {
    position: absolute;
    left: 128px;
    top: 323px;
    font-weight: 800;
    font-size: 34px;
    line-height: 1;
    color: var(--ink);
    white-space: nowrap;
  }
  .appointment__title {
    position: absolute;
    left: 458px;
    top: 182px;
    font-weight: 800;
    font-size: 46px;
    line-height: 1;
    letter-spacing: 0.3px;
  }
  .fields { list-style: none; }
  .field {
    position: absolute;
    left: 487px;
    font-weight: 500;
    font-size: 37px;
    line-height: 1;
    white-space: nowrap;
  }
  .field::before {
    content: "";
    position: absolute;
    left: -25px;
    top: 17px;
    width: 8px;
    height: 8px;
    border-radius: 50%;
    background: var(--ink);
  }
  .field--date  { top: 262px; }
  .field--time  { top: 326px; }
  .field--rep   { top: 400px; }
  .field--phone { top: 465px; }
  .field__blank {
    position: absolute;
    top: 33px;
    height: 0;
    border-bottom: 2px solid var(--ink);
  }
  .field--date .field__blank  { left: 119px; width: 289px; }
  .field--time .field__blank  { left: 115px; width: 336px; }
  .field--rep .field__blank   { left: 302px; width: 288px; }
  .field--phone .field__blank { left: 140px; width: 288px; }
</style>
</head>
<body>
  <div class="page">
    <div class="card"></div>
    <div class="card__frame"></div>

    <div class="brand-name">Sunridge Solar</div>

    <h1 class="appointment__title">APPOINTMENT</h1>
    <ul class="fields">
      <li class="field field--date">Date:<span class="field__blank"></span></li>
      <li class="field field--time">Time:<span class="field__blank"></span></li>
      <li class="field field--rep">Representative:<span class="field__blank"></span></li>
      <li class="field field--phone">Phone:<span class="field__blank"></span></li>
    </ul>
  </div>
</body>
</html>
```